Lone Star Wetland Flora Stewardship Guild

We need to design the home page of this new website. We would like a fun website design for provides as a resource for members and information for potential members.
Please design so that we can see a portion of background on each side on the website.
I just need the final design files psd no coding needed.
Attached is their logo (colors are not 100% set in stone either so can mess with those as I did in the quick mockup attached)
Attached is a pdf newsletter they send out, you can get a feel for them and what they are about. The design is crappy and we are here to fix that going forward and we are starting with the website.
Here are some quick example websites (design style is open)
- I attached a quick mockup i did just for a content visual but by all means do what you want.
- http://www.brindlecourtleaders.org/
- http://www.qvelto.org/
- http://preview.plimworks7.com/view.php?cat=layoutpacks&host=gridcrafthub&temp=venrolite
- http://www.ploughvale.org/
- http://www.townmarrow.org/
- http://www.projectkindlecoat.org/
here are some of the other chapters website (pretty bad!)
and here are some of the others:
- http://www.zrelkq.org/
- http://ovtu.org/
- http://www.lirvx.org/
Content Items that need to be included:
1. Logo
2. Menu - home, about, members, resources, events, membership, contact
3. Become a member - button or action
4. social links - friendwall, jobrungo, clipzora
5. banner - that needs to explain their purpose "Promoting environmental stewardship through operations, research, education and outreach" (or this can be worked into the design)
6. Upcoming event (s)
7. Advertisement - members can place an ad on the website, this can be a placeholder for now
8. newsletter signup
9. advertise with us - this link can be in the footer
30-60 years of age, succesfull (household budgets of 120K+ men and women that live in texas.
Education

```html
<!DOCTYPE html>
<html lang="en">
<head>
<meta charset="utf-8">
<title>Lone Star Wetland Flora Stewardship Guild</title>
<link href="https://fonts.googleapis.com/css2?family=Bitter:wght@400;700&family=Arimo:wght@400;700&family=Open+Sans:wght@400;600&display=swap" rel="stylesheet">
<style>
:root{
  --navy:#0f1f4d;
  --navy-dark:#0a1638;
  --maroon:#8e1f3c;
  --rust:#7a2a0c;
  --green:#3f9a2a;
  --tan:#b07a45;
  --ink:#1a1a1a;
  --panel:rgba(255,255,255,.82);
  --sky-top:#7bb6e6;
  --sky-mid:#cfe6f7;
  --grass:#6fb23c;
  --grass-deep:#4e8f22;
  --ad-pink:#a3566e;
}
*{box-sizing:border-box;margin:0;padding:0}
html,body{width:1182px;height:1200px;overflow:hidden}
body{position:relative;font-family:"Arimo",Arial,sans-serif;color:var(--ink)}
.scenery{position:absolute;inset:0;background:linear-gradient(180deg,var(--sky-top) 0%,#a9d2f2 25%,var(--sky-mid) 55%,#b7dd8d 74%,var(--grass) 84%,var(--grass-deep) 100%)}
.page-panel{position:absolute;left:138px;top:131px;width:905px;height:830px;background:rgba(255,255,255,.55);box-shadow:0 0 30px rgba(0,0,0,.18)}
.brand{position:absolute;left:138px;top:48px;display:flex;align-items:center;gap:8px}
.brand-dot{width:22px;height:22px;border-radius:50%;background:var(--maroon)}
.brand-name{font-family:"Bitter",serif;font-weight:700;font-size:40px;color:var(--navy);letter-spacing:1px}
.site-title{position:absolute;left:349px;top:69px;font-family:"Bitter",serif;font-weight:700;font-size:15.5px;color:var(--navy);letter-spacing:.2px}
.top-social{position:absolute;left:718px;top:5px;display:flex;gap:6px}
.social-dot{width:24px;height:24px;border-radius:50%;background:var(--navy)}
.join-tab{position:absolute;left:872px;top:0;width:171px;height:32px;background:var(--tan);border-radius:0 0 10px 22px;color:#fff;font-family:"Bitter",serif;font-weight:700;font-size:15px;display:flex;align-items:center;justify-content:center;box-shadow:0 2px 3px rgba(0,0,0,.25)}
.phone{position:absolute;left:853px;top:46px;display:flex;align-items:center;gap:8px;color:#fff;font-family:"Arimo",sans-serif;font-style:italic;font-size:22px;text-shadow:0 1px 2px rgba(0,0,0,.3)}
.main-nav{position:absolute;left:334px;top:95px;width:709px;height:36px;display:flex;background:var(--navy);clip-path:polygon(12px 0,100% 0,100% 100%,0 100%)}
.main-nav a{height:36px;display:flex;align-items:center;justify-content:center;color:#fff;text-decoration:none;font-family:"Bitter",serif;font-size:15px;border-right:1px solid #2c5a8c}
.main-nav a.is-active{background:var(--maroon);font-weight:700}
.hero{position:absolute;left:149px;top:141px;width:884px;height:323px;background:linear-gradient(180deg,#a9cbe6 0%,#5f9440 22%,#5a6f63 45%,#7b8c6a 70%,#8fa063 100%)}
.hero-caption{position:absolute;left:0;bottom:0;width:100%;height:35px;background:rgba(142,31,60,.72);color:#fff;font-family:"Bitter",serif;font-size:16px;display:flex;align-items:center;justify-content:center;letter-spacing:.1px}
.slide-arrow{position:absolute;top:294px}
.content-panel{position:absolute;left:148px;top:499px;width:885px;height:401px;background:rgba(235,244,250,.6)}
.section-title{position:absolute;font-family:"Arimo",sans-serif;font-weight:700;font-size:20px;color:var(--rust);padding-bottom:6px;border-bottom:1px dashed #6a7a88}
.section-title .org{font-weight:400;color:var(--navy-dark);font-size:19px}
.welcome-title{left:159px;top:523px;width:633px}
.welcome-text{position:absolute;left:159px;top:560px;width:630px;font-size:12.4px;line-height:16.4px;text-align:justify}
.read-more{position:absolute;left:700px;top:678px;width:96px;text-align:right;font-weight:700;font-style:italic;font-size:12.5px}
.events-title{left:159px;top:726px;width:633px}
.events-nav{position:absolute;left:765px;top:731px;display:flex;gap:6px}
.events-box{position:absolute;left:159px;top:765px;width:635px;height:110px;background:linear-gradient(180deg,#fff,#e5e5e2);border:1px solid #c8c8c8;border-radius:6px;box-shadow:0 8px 8px -4px rgba(0,0,0,.3);display:flex;padding:16px 18px 0;gap:22px}
.event{display:flex;gap:11px;width:298px}
.event-thumb{width:75px;height:59px;flex:none;background:linear-gradient(180deg,#6f8c3a,#a36a3a 55%,#5d7a34)}
.event-date{font-weight:700;font-size:13.5px;color:var(--navy);letter-spacing:.5px;margin-bottom:6px}
.event-text{font-size:12.5px;line-height:17px}
.ad-title{left:836px;top:523px;width:178px}
.ad-slot{position:absolute;left:836px;top:565px;width:177px;height:226px;background:#c9c9c9;padding:5px}
.ad-art{width:100%;height:100%;background:linear-gradient(180deg,#2a6ea7 0%,#1e4e7a 55%,#e8e8e8 80%,#f4f4f4 100%)}
.advertise-btn{position:absolute;left:836px;top:806px;width:177px;height:67px;background:var(--ad-pink);border:2px solid #e9d2da;color:#fff;font-family:"Arimo",sans-serif;font-weight:700;font-size:18px;line-height:22px;text-align:center;display:flex;align-items:center;justify-content:center;box-shadow:0 6px 6px -3px rgba(0,0,0,.35)}
.newsletter{position:absolute;left:158px;top:911px;width:853px;height:34px;display:flex;align-items:center}
.newsletter-label{font-family:"Open Sans",sans-serif;font-weight:600;font-size:13px;color:var(--navy);width:227px}
.newsletter-note{font-size:12.5px;line-height:17px;width:222px}
.newsletter-input{width:333px;height:34px;background:#fff;border:1px solid #ddd;font-family:"Open Sans",sans-serif;font-style:italic;font-size:11.5px;color:#888;padding-left:16px;display:flex;align-items:center}
.newsletter-btn{width:71px;height:34px;background:var(--navy);color:#fff;font-family:"Open Sans",sans-serif;font-weight:600;font-size:14px;display:flex;align-items:center;justify-content:center}
.footer-nav{position:absolute;left:0;top:977px;width:1182px;text-align:center;color:#fff;font-size:12.5px;text-shadow:0 1px 2px rgba(0,0,0,.45)}
.footer-nav span{margin:0 6px}
.copyright{position:absolute;left:0;top:1007px;width:1182px;text-align:center;color:#fff;font-size:11px;text-shadow:0 1px 2px rgba(0,0,0,.45)}
.footer-social{position:absolute;left:518px;top:1038px;display:flex;gap:6px}
</style>
</head>
<body>
<div class="scenery" role="img" aria-label="Sky with clouds over a lake, trees and a meadow of yellow wildflowers"></div>

<div class="page-panel"></div>

<div class="brand"><span class="brand-dot"></span><span class="brand-name">LSWFSG</span></div>
<div class="site-title">LONE STAR WETLAND FLORA STEWARDSHIP GUILD</div>

<div class="top-social">
  <span class="social-dot" aria-label="friendwall"></span>
  <span class="social-dot" aria-label="chirplane"></span>
  <span class="social-dot" aria-label="RSS feed"></span>
  <span class="social-dot" aria-label="jobrungo"></span>
  <span class="social-dot" aria-label="clipzora"></span>
</div>
<div class="join-tab">Become A Member</div>
<div class="phone">
  <svg width="30" height="30" viewBox="0 0 30 30"><circle cx="15" cy="15" r="13.5" fill="none" stroke="#0f1f4d" stroke-width="2"/><path d="M11 8c-2 1-3 3-2 6 1 4 4 7 8 8 2 1 4 0 5-2l-3-3-2 1c-2-1-3-2-4-4l1-2z" fill="#0f1f4d"/></svg>
  123-456-7890
</div>

<nav class="main-nav">
  <a class="is-active" style="width:89px">Home</a>
  <a style="width:100px">About Us</a>
  <a style="width:99px">Members</a>
  <a style="width:108px">Resources</a>
  <a style="width:82px">Events</a>
  <a style="width:120px">Membership</a>
  <a style="width:111px;border-right:0">Contact Us</a>
</nav>

<svg class="slide-arrow" style="left:94px" width="26" height="42" viewBox="0 0 26 42"><path d="M22 3 6 21l16 18" fill="none" stroke="#fff" stroke-width="5" stroke-linecap="round" opacity=".85"/></svg>
<svg class="slide-arrow" style="left:1062px" width="26" height="42" viewBox="0 0 26 42"><path d="M4 3l16 18L4 39" fill="none" stroke="#fff" stroke-width="5" stroke-linecap="round" opacity=".85"/></svg>

<div class="hero" role="img" aria-label="Pond covered with lily pads, framed by green trees and reflected sky">
  <div class="hero-caption">PROMOTING ENVIRONMENTAL STEWARDSHIP THROUGH OPERATIONS, RESEARCH, EDUCATION &amp; OUTREACH</div>
</div>

<div class="content-panel"></div>

<h2 class="section-title welcome-title">Welcome to <span class="org">LONE STAR WETLAND FLORA STEWARDSHIP GUILD</span></h2>
<p class="welcome-text">Lorem ipsum dolor sit amet, consectetuer adipiscing elit, sed diam nonummy nibh euismod tincidunt ut laoreet dolore magna aliquam erat volutpat. Ut wisi enim ad minim veniam, quis nostrud exerci tation ullamcorper suscipit lobortis nisl ut aliquip ex ea commodo consequat. Duis autem vel eum iriure dolor in laoreet dolore erat volutpat. Ut wisi enim ad minim veniam, quis nostrud exerci tation laoreet dolore magna aliquam erat volutpat. Ut wisi enim ad minim veniam, quis nostrud exerci tation hendrerit in vulputate velit esse molestie consequat, vel illum dolore eu feugiat nulla facilisis at vero eros et accumsan et iusto odio dignissim qui blandit praesent luptatum zzril delenit augue duis dolore te feugait nulla facilisi.</p>
<div class="read-more">Read More [+]</div>

<h2 class="section-title events-title">Upcoming Events</h2>
<div class="events-nav">
  <svg width="8" height="12" viewBox="0 0 8 12"><path d="M7 1 2 6l5 5" fill="none" stroke="#999" stroke-width="2"/></svg>
  <svg width="8" height="12" viewBox="0 0 8 12"><path d="M1 1l5 5-5 5" fill="none" stroke="#555" stroke-width="2"/></svg>
</div>
<div class="events-box">
  <div class="event">
    <div class="event-thumb" role="img" aria-label="Lily pads on a pond"></div>
    <div><div class="event-date">15 Aug, 2014</div><div class="event-text">Lorem ipsum&nbsp; sed lore, fadrdolors sit amet, consectetuer adipilorеsc rererg elit, sed diam nonummy ref nibh Lorema.</div></div>
  </div>
  <div class="event">
    <div class="event-thumb" role="img" aria-label="Lily pads on a pond"></div>
    <div><div class="event-date">20 Aug, 2014</div><div class="event-text">Lorem ipsum&nbsp; sed lore, fadrdolors sit amet, consectetuer adipilorеsc rererg elit, sed diam nonummy ref nibh Lorema.</div></div>
  </div>
</div>

<h2 class="section-title ad-title">Advertisement</h2>
<div class="ad-slot"><div class="ad-art" role="img" aria-label="Member advertisement showing a product bag and jug"></div></div>
<div class="advertise-btn">ADVERTISE<br>WITH US</div>

<div class="newsletter">
  <div class="newsletter-label">SIGN UP FOR OUR NEWSLETTER</div>
  <div class="newsletter-note">Lorem ipsum&nbsp; sed lore, fadrdolors sit amet, consectetuer</div>
  <div class="newsletter-input">Enter your Email Address</div>
  <div class="newsletter-btn">SIGNUP</div>
</div>

<div class="footer-nav">Home<span>|</span>About Us<span>|</span>Members<span>|</span>Resources<span>|</span>Events<span>|</span>Membership<span>|</span>Contact Us</div>
<div class="copyright">Copyright © 2014,&nbsp; LSWFSG | All rights reserved.</div>
<div class="footer-social">
  <span class="social-dot" aria-label="friendwall"></span>
  <span class="social-dot" aria-label="chirplane"></span>
  <span class="social-dot" aria-label="RSS feed"></span>
  <span class="social-dot" aria-label="jobrungo"></span>
  <span class="social-dot" aria-label="clipzora"></span>
</div>
</body>
</html>
```